New Interfaces

The software open with 3 open tabs, you can see the interfaces following this steps:

Zonvia:
Select tab "Zonvia" and click on "Zonvia" in menu on the top.

KPI :
Select tab "KPI" and click on go button.

Report:
Select tab "Report" and Click on go button.

Current software: http://plexora.kelvoxsoft.net/plexora_developers/default.aspx

user: review_guest
pass: lumbrak

......

About the company

The Kelvox is a technology company that provides planning, optimization services and software to develop the market for telecom operators.

The Product

Plexora is a web management and optimization tool for mobile networks.

The project

To always offer the best experience of usability and comfort for our customers, we are remodeling our software. The goal is to have agile, modern and with special attention to usability interfaces.

user: review_guest
pass: lumbrak
Updates

Hi! We are analyzing all interfaces, we send news soon. Thank you!

Target Market(s)

Telecommunications Engineers.

Industry/Entity Type

Software

Font styles to use
Sans Serif

Requirements
Nice to have
• Attention for usability and good concept.
Should not have
• Many colors.

```html
<!DOCTYPE html>
<html lang="en">
<head>
<meta charset="utf-8">
<title>Kelvox · Account Preferences</title>
<link rel="stylesheet" href="https://fonts.googleapis.com/css2?family=Roboto:wght@400;500;700&display=swap">
<style>
:root{
  --ink:#333;--muted:#777;--orange:#e0823a;--blue:#0d4f86;--dark:#1b1b1b;--side:#323232;--side-2:#3d3d3d;
  --panel:#fafafa;--line:#d5d5d5;--bg:#efefef;--row-alt:#d8d8d8;--white:#fff;
}
*{box-sizing:border-box;margin:0;padding:0}
html,body{width:716px;height:1200px;overflow:hidden}
body{position:relative;font-family:"Roboto",Arial,sans-serif;font-size:7px;color:var(--ink);background:var(--bg)}
.abs{position:absolute}
.topbar{left:0;top:0;width:716px;height:34px;background:var(--dark)}
.search{left:7px;top:8px;width:87px;height:16px;border:1px solid #777;background:#2a2a2a;color:#bbb;padding:3px 5px;font-size:7px}
.menu{left:102px;top:0;height:34px;display:flex;gap:2px}
.menu span{display:flex;align-items:center;gap:3px;height:34px;padding:0 5px;background:#262626;color:#eee;font-size:7px;white-space:nowrap}
.menu i{width:6px;height:6px;border-radius:50%;background:#ddd;display:inline-block}
.exit{left:688px;top:0;width:28px;height:34px;background:var(--orange)}
.brand{left:0;top:34px;width:102px;height:44px;background:#e9e9e9;display:flex;align-items:center;justify-content:center;gap:4px;font-size:16px;font-weight:700;color:var(--blue)}
.brand b{width:7px;height:7px;background:var(--orange);display:block}
.rail{left:0;top:78px;width:22px;height:1078px;background:#2a2a2a}
.tree{left:22px;top:78px;width:80px;height:1078px;background:var(--side-2)}
.tree-top{left:22px;top:78px;width:80px;height:280px;background:var(--side)}
.vtab{left:0;width:19px;color:#fff;font-size:7px;writing-mode:vertical-rl;display:flex;align-items:center;justify-content:center}
.tree-label{color:#bbb;font-size:6px}
.tree-label em{color:var(--orange);font-style:normal}
.group{left:22px;width:80px;height:22px;background:#474747;color:#fff;font-size:6px;padding:0 6px;display:flex;align-items:center;gap:3px}
.node{color:#ddd;font-size:6px;display:flex;align-items:center;gap:3px}
.node i{width:4px;height:4px;border-radius:50%;border:1px solid #aaa;display:block}
.node.on{left:22px;width:80px;height:13px;background:var(--orange);color:#fff;padding-left:22px}
.footer{left:0;top:1156px;width:716px;height:44px;background:var(--dark);color:#999;font-size:6.5px}
.tab{top:44px;height:22px;font-size:7px;display:flex;align-items:center;justify-content:center;border:1px solid var(--line)}
.btn{display:flex;align-items:center;justify-content:center;font-size:6.5px;color:#fff;border-radius:2px;position:absolute}
.b-blue{background:var(--blue)}.b-orange{background:var(--orange)}.b-dark{background:#333}
.b-gray{background:#ddd;color:#444;border:1px solid #c5c5c5}
.panel{left:114px;width:592px;background:var(--panel);border:1px solid var(--line)}
.phead{left:114px;width:592px;height:22px;background:#e6e6e6;border-bottom:1px solid var(--line);font-size:7.5px;display:flex;align-items:center;padding-left:8px;gap:6px}
.phead .x{color:var(--orange)}
.inner{background:#fff;border:1px solid var(--line)}
.label{left:134px;font-size:6.5px;color:#555}
.field{left:202px;width:102px;height:19px;border:1px solid #bbb;background:#fff;box-shadow:inset 0 1px 2px rgba(0,0,0,.12);font-size:6px;color:#888;padding:5px 7px}
.bar{left:120px;width:580px;height:24px;background:#e8e8e8;border:1px solid var(--line);font-size:7px;display:flex;align-items:center;padding-left:10px;gap:6px}
.tt{left:124px;top:579px;width:572px;border-collapse:collapse;table-layout:fixed;font-size:6.3px;text-align:center}
.tt th{background:var(--orange);color:#fff;font-weight:400;height:25px;border-right:1px solid #f0b58a}
.tt td{height:35.2px;line-height:1.45}
.tt tr:nth-child(even) td{background:var(--row-alt)}
.tt tr:nth-child(odd) td{background:#fff}
.tt td:first-child span{display:inline-block;width:7px;height:7px;border:1px solid #aaa;background:#fff}
.tt u{color:#333}
.pg{top:999px;height:16px;border:1px solid #ccc;background:#f7f7f7;font-size:6.5px;display:flex;align-items:center;justify-content:center;color:#555}
.pg.on{background:var(--orange);color:#fff;border-color:var(--orange)}
.sel{height:18px;border:1px solid #bbb;background:#fff;font-size:6px;padding:4px 6px;color:#555}
.stat{top:1059px;height:15px;font-size:6.5px;display:flex;align-items:center;justify-content:center;border:1px solid #ccc;background:#fff}
.stat.g{background:#d6d6d6}
.small{font-size:6.5px;color:#555}
</style>
</head>
<body>
<header class="abs topbar"></header>
<div class="abs search">Search...</div>
<nav class="abs menu">
  <span><i></i>Configuration</span><span><i></i>Statistics</span><span><i></i>Planned Network</span><span><i></i>Main KPIs</span><span><i></i>Reports</span><span><i></i>Zonvia</span><span><i></i>Work Orders</span><span><i></i>Support</span><span><i></i>Custom</span><span><i></i>My View</span><span><i></i>Help</span>
</nav>
<div class="abs exit"><svg width="28" height="34" viewBox="0 0 28 34"><path d="M9 17h8M14 13l4 4-4 4M17 11h3v12h-3" stroke="#fff" stroke-width="1.6" fill="none"/></svg></div>

<div class="abs brand"><b></b>Kelvox</div>
<aside class="abs rail"></aside>
<aside class="abs tree"></aside>
<div class="abs tree-top"></div>
<div class="abs vtab b-orange" style="top:86px;height:44px">Treeview</div>
<div class="abs vtab b-blue" style="top:136px;height:58px">Workspaces</div>
<div class="abs vtab b-blue" style="top:200px;height:45px">Zonvia</div>
<div class="abs tree-label" style="left:30px;top:89px">Tree Mode : &nbsp;<em>Today</em></div>
<div class="abs group" style="top:104px">▣ Real Network ▾</div>
<div class="abs node" style="left:34px;top:131px"><i></i>NORVIK</div>
<div class="abs node" style="left:44px;top:142px"><i></i>2G</div>
<div class="abs node" style="left:44px;top:154px"><i></i>3G</div>
<div class="abs node on" style="top:162px"><i></i>LTE</div>
<div class="abs node" style="left:44px;top:178px"><i></i>CORE PS</div>
<div class="abs node" style="left:44px;top:191px"><i></i>SAE-GW</div>
<div class="abs node" style="left:44px;top:203px"><i></i>MME</div>
<div class="abs node" style="left:34px;top:218px"><i></i>HUANLO</div>
<div class="abs node" style="left:34px;top:233px"><i></i>ERDMANN</div>
<div class="abs node" style="left:34px;top:248px"><i></i>ZTX</div>
<div class="abs node" style="left:34px;top:263px"><i></i>MULTIVENDOR</div>
<div class="abs node" style="left:34px;top:279px"><i></i>ALTERON</div>
<div class="abs group" style="top:299px;height:20px">▣ Planned Network ▾</div>
<div class="abs node" style="left:34px;top:327px"><i></i>Public Network</div>
<div class="abs node" style="left:34px;top:342px"><i></i>Private Network</div>

<div class="abs tab" style="left:110px;width:54px;background:#fff;color:var(--blue)">(New Tab)</div>
<div class="abs tab" style="left:166px;width:44px;top:48px;height:15px;color:#aaa;background:#fff">+ Tab</div>
<svg class="abs" style="left:222px;top:49px" width="12" height="12"><rect x="1" y="1" width="10" height="10" fill="#5a9a4a"/></svg>
<svg class="abs" style="left:244px;top:49px" width="12" height="12"><rect x="1" y="1" width="10" height="10" fill="#c33"/></svg>
<div class="btn b-blue" style="left:264px;top:48px;width:43px;height:15px">GO ALL</div>

<section class="abs panel" style="top:74px;height:346px"></section>
<div class="abs phead" style="top:74px"><span class="x">× +</span>Account Preferences</div>
<div class="btn b-dark" style="left:222px;top:80px;width:34px;height:13px">SAVE</div>
<div class="abs inner" style="left:120px;top:102px;width:580px;height:302px"></div>
<div class="btn b-blue" style="left:125px;top:108px;width:86px;height:20px;border-radius:0">User Preferences</div>
<div class="btn b-orange" style="left:217px;top:108px;width:86px;height:20px;border-radius:0">Chart Preferences</div>
<div class="btn b-orange" style="left:307px;top:108px;width:94px;height:20px;border-radius:0">Interface Preferences</div>
<div class="abs" style="left:120px;top:128px;width:580px;height:1px;background:var(--line)"></div>
<div class="abs label" style="top:152px">User Name :</div><div class="abs field" style="top:146px">review_guest</div>
<div class="abs label" style="top:182px">Full Name :</div><div class="abs field" style="top:176px">review_guest</div>
<div class="abs label" style="top:212px">Phone :</div><div class="abs field" style="top:206px"></div>
<div class="abs label" style="top:242px">E-mail :</div><div class="abs field" style="top:236px">teo.ramos@kelvox.com</div>
<div class="abs label" style="top:272px">Old Password :</div><div class="abs field" style="top:266px"></div>
<div class="abs label" style="top:302px">New Password :</div><div class="abs field" style="top:296px"></div>
<div class="abs label" style="top:332px">Repeat Password :</div><div class="abs field" style="top:326px"></div>
<div class="abs label" style="top:368px">Receive Update Emails</div>
<div class="btn b-blue" style="left:216px;top:364px;width:31px;height:16px">YES</div>
<div class="btn b-orange" style="left:254px;top:364px;width:33px;height:16px">NO</div>

<section class="abs panel" style="top:437px;height:653px"></section>
<div class="abs phead" style="top:437px"><span class="x">× +</span>Trouble Tickets (TT)</div>
<div class="btn b-gray" style="left:126px;top:474px;width:46px;height:17px">NEW</div>
<div class="btn b-gray" style="left:178px;top:474px;width:90px;height:17px">SHOW MONITORED</div>
<div class="abs small" style="left:278px;top:479px">Text or ID :</div>
<div class="abs field" style="left:316px;top:474px;width:74px;height:17px"></div>
<div class="btn b-blue" style="left:394px;top:474px;width:48px;height:17px">SHOW IT</div>
<div class="abs bar" style="top:502px">▸ Selected TT</div>
<div class="abs bar" style="top:531px">▾ Search Results</div>
<div class="abs inner" style="left:120px;top:557px;width:580px;height:527px;border:none"></div>
<div class="abs" style="left:124px;top:565px;width:572px;text-align:center;font-size:8px">FILTER RESULTS</div>
<table class="abs tt">
<colgroup><col style="width:18px"><col style="width:27px"><col style="width:20px"><col style="width:25px"><col style="width:31px"><col style="width:94px"><col style="width:62px"><col style="width:107px"><col style="width:80px"><col style="width:108px"></colgroup>
<thead><tr><th></th><th>ID</th><th>N</th><th>Priority</th><th>Days</th><th>Status</th><th>Problem ID</th><th>Description</th><th>Updated</th><th>Opened By</th></tr></thead>
<tbody>
<tr><td><span></span></td><td><u>1585</u></td><td>2</td><td>None</td><td>7</td><td>Feedback<br>([Kelvox] Support_Team)</td><td>New Feature<br>Request</td><td>Editar od estilos Do Plexora<br>atual Co...</td><td>2014-12-03 15:59:54</td><td>[Kelvox] Support_Team<br>(To: [Kelvox] support_Team)</td></tr>
<tr><td><span></span></td><td><u>1585</u></td><td>2</td><td>None</td><td>7</td><td>Feedback<br>([Kelvox] Support_Team)</td><td>New Feature<br>Request</td><td>Editar od estilos Do Plexora<br>atual Co...</td><td>2014-12-03 15:59:54</td><td>[Kelvox] Support_Team<br>(To: [Kelvox] support_Team)</td></tr>
<tr><td><span></span></td><td><u>1585</u></td><td>2</td><td>None</td><td>7</td><td>Feedback<br>([Kelvox] Support_Team)</td><td>New Feature<br>Request</td><td>Editar od estilos Do Plexora<br>atual Co...</td><td>2014-12-03 15:59:54</td><td>[Kelvox] Support_Team<br>(To: [Kelvox] support_Team)</td></tr>
<tr><td><span></span></td><td><u>1585</u></td><td>2</td><td>None</td><td>7</td><td>Feedback<br>([Kelvox] Support_Team)</td><td>New Feature<br>Request</td><td>Editar od estilos Do Plexora<br>atual Co...</td><td>2014-12-03 15:59:54</td><td>[Kelvox] Support_Team<br>(To: [Kelvox] support_Team)</td></tr>
<tr><td><span></span></td><td><u>1585</u></td><td>2</td><td>None</td><td>7</td><td>Feedback<br>([Kelvox] Support_Team)</td><td>New Feature<br>Request</td><td>Editar od estilos Do Plexora<br>atual Co...</td><td>2014-12-03 15:59:54</td><td>[Kelvox] Support_Team<br>(To: [Kelvox] support_Team)</td></tr>
<tr><td><span></span></td><td><u>1585</u></td><td>2</td><td>None</td><td>7</td><td>Feedback<br>([Kelvox] Support_Team)</td><td>New Feature<br>Request</td><td>Editar od estilos Do Plexora<br>atual Co...</td><td>2014-12-03 15:59:54</td><td>[Kelvox] Support_Team<br>(To: [Kelvox] support_Team)</td></tr>
<tr><td><span></span></td><td><u>1585</u></td><td>2</td><td>None</td><td>7</td><td>Feedback<br>([Kelvox] Support_Team)</td><td>New Feature<br>Request</td><td>Editar od estilos Do Plexora<br>atual Co...</td><td>2014-12-03 15:59:54</td><td>[Kelvox] Support_Team<br>(To: [Kelvox] support_Team)</td></tr>
<tr><td><span></span></td><td><u>1585</u></td><td>2</td><td>None</td><td>7</td><td>Feedback<br>([Kelvox] Support_Team)</td><td>New Feature<br>Request</td><td>Editar od estilos Do Plexora<br>atual Co...</td><td>2014-12-03 15:59:54</td><td>[Kelvox] Support_Team<br>(To: [Kelvox] support_Team)</td></tr>
<tr><td><span></span></td><td><u>1585</u></td><td>2</td><td>None</td><td>7</td><td>Feedback<br>([Kelvox] Support_Team)</td><td>New Feature<br>Request</td><td>Editar od estilos Do Plexora<br>atual Co...</td><td>2014-12-03 15:59:54</td><td>[Kelvox] Support_Team<br>(To: [Kelvox] support_Team)</td></tr>
<tr><td><span></span></td><td><u>1585</u></td><td>2</td><td>None</td><td>7</td><td>Feedback<br>([Kelvox] Support_Team)</td><td>New Feature<br>Request</td><td>Editar od estilos Do Plexora<br>atual Co...</td><td>2014-12-03 15:59:54</td><td>[Kelvox] Support_Team<br>(To: [Kelvox] support_Team)</td></tr>
<tr><td><span></span></td><td><u>1585</u></td><td>2</td><td>None</td><td>7</td><td>Feedback<br>([Kelvox] Support_Team)</td><td>New Feature<br>Request</td><td>Editar od estilos Do Plexora<br>atual Co...</td><td>2014-12-03 15:59:54</td><td>[Kelvox] Support_Team<br>(To: [Kelvox] support_Team)</td></tr>
</tbody>
</table>
<div class="abs pg" style="left:126px;width:30px">Prev</div>
<div class="abs pg on" style="left:161px;width:16px">1</div>
<div class="abs pg" style="left:182px;width:16px">2</div>
<div class="abs pg" style="left:202px;width:16px">3</div>
<div class="abs pg" style="left:223px;width:16px">4</div>
<div class="abs pg" style="left:243px;width:16px">5</div>
<div class="abs pg" style="left:264px;width:16px">6</div>
<div class="abs pg" style="left:285px;width:16px">...</div>
<div class="abs pg" style="left:305px;width:16px">22</div>
<div class="abs pg" style="left:324px;width:32px">Next</div>
<div class="abs inner" style="left:126px;top:1022px;width:569px;height:31px"></div>
<div class="abs small" style="left:136px;top:1034px;display:flex;gap:4px;align-items:center"><span style="width:7px;height:7px;border:1px solid #aaa;display:block"></span>Select All</div>
<div class="abs sel" style="left:178px;top:1029px;width:102px">Update Priority<span style="float:right">⇕</span></div>
<div class="abs sel" style="left:286px;top:1029px;width:101px">None<span style="float:right">⇕</span></div>
<div class="btn b-blue" style="left:394px;top:1029px;width:29px;height:18px">GO</div>
<div class="abs stat" style="left:126px;width:50px">Open</div>
<div class="abs stat g" style="left:180px;width:52px">Assigned</div>
<div class="abs stat" style="left:234px;width:54px">Feedback</div>
<div class="abs stat g" style="left:290px;width:66px">Acknowledged</div>
<div class="abs stat" style="left:358px;width:68px">Confirmed</div>
<div class="abs stat g" style="left:428px;width:66px">Resolved</div>
<div class="abs stat" style="left:496px;width:66px">Closed</div>

<section class="abs panel" style="top:1099px;height:51px"></section>
<div class="abs phead" style="top:1099px"><span class="x">× +</span>Chart - DL MCS TBs</div>
<div class="btn b-orange" style="left:220px;top:1103px;width:37px;height:14px">DY</div>
<div class="abs" style="left:272px;top:1107px;font-size:6.5px;color:var(--blue)">☰ OPTIONS</div>
<div class="abs small" style="left:332px;top:1107px">FROM</div>
<div class="abs field" style="left:354px;top:1103px;width:52px;height:15px;padding:3px 5px">2014-12-01</div>
<div class="abs small" style="left:414px;top:1107px">TO</div>
<div class="abs field" style="left:428px;top:1103px;width:51px;height:15px;padding:3px 5px">2014-12-01</div>
<div class="btn b-blue" style="left:487px;top:1103px;width:23px;height:14px">GO</div>

<footer class="abs footer"><span class="abs" style="left:108px;top:17px">Copyrights © 2014 &nbsp; All Rights Reserved</span><span class="abs" style="left:678px;top:17px;color:#fff;font-size:7.5px">C6</span></footer>
</body>
</html>
```